Meridian Rest Supply Needs Business Card

Looking for a very nice looking business card. Creative but not extravagant. We sell beds and pillows across the U.S. and need something professional but catchy. I have attached the logo.

Name : Dale Fenwick
Title : President
Phone : (800) 417-2964
Email: sleep@quorvana.com
Website: www.quorvana.com

Can be single-sided or double-sided
horizontal or vertical

Can use Blues/Greys

Target Market(s)

Mass Market

Industry/Entity Type

Retail

Contact Information for Business Card

Name : Dale Fenwick
Title : President
Phone : (800) 417-2964
Email: sleep@quorvana.com
Website: www.quorvana.com

Requirements
Must have
• Clean, Modern, Smooth
• Can use Blues/Greys
• On the other side without the information - have something simple like www.quorvana.com or our logo
Nice to have
• Surprise me
Should not have
• Nothing crazy, nothing cluttered

```html
<!DOCTYPE html>
<html lang="en">
<head>
<meta charset="utf-8">
<title>Meridian Rest Supply – Business Card</title>
<link rel="stylesheet" href="https://fonts.googleapis.com/css2?family=Roboto+Slab:wght@300;400;500&display=swap">
<style>
  :root {
    --backdrop: #9a9a9a;
    --card: #f7f7f5;
    --ink: #151515;
    --accent: #2a94cf;
  }
  html, body {
    margin: 0;
    padding: 0;
    width: 1200px;
    height: 800px;
    overflow: hidden;
    background: var(--backdrop);
  }
  .canvas {
    position: relative;
    width: 1200px;
    height: 800px;
    display: flex;
    align-items: center;
    justify-content: center;
  }
  .business-card {
    width: 840px;
    height: 480px;
    background: var(--card);
    border-radius: 40px;
    display: flex;
    flex-direction: column;
    align-items: center;
    box-sizing: border-box;
    padding-top: 150px;
    font-family: "Roboto Slab", serif;
    color: var(--ink);
  }
  .wordmark {
    margin: 0;
    font-family: "Roboto Slab", serif;
    font-weight: 300;
    font-size: 62px;
    letter-spacing: 1px;
    color: var(--accent);
    line-height: 1;
  }
  .holder-name {
    margin: 34px 0 0;
    font-size: 28px;
    font-weight: 500;
    line-height: 1.1;
  }
  .holder-title {
    margin: 2px 0 0;
    font-size: 20px;
    font-weight: 400;
    color: var(--accent);
  }
  .contact-row {
    display: flex;
    gap: 22px;
    margin-top: 30px;
    font-size: 20px;
  }
  .contact-item {
    display: flex;
    align-items: center;
    gap: 6px;
  }
  .contact-icon {
    width: 24px;
    height: 24px;
    flex: none;
  }
</style>
</head>
<body>
<main class="canvas">
  <section class="business-card" aria-label="Business card for Dale Fenwick">
    <h1 class="wordmark">www.quorvana.com</h1>
    <p class="holder-name">Dale Fenwick</p>
    <p class="holder-title">President</p>
    <div class="contact-row">
      <span class="contact-item">
        <svg class="contact-icon" viewBox="0 0 24 24" aria-hidden="true">
          <circle cx="12" cy="12" r="10.5" fill="none" stroke="var(--accent)" stroke-width="1.6"/>
          <path d="M9 6.5c-.8.3-1.6 1.2-1.5 2.5.2 3.4 4.1 7.9 7.4 8.6 1.2.2 2.1-.4 2.5-1.2l-2-1.8-1.3 1c-1.6-.7-3.3-2.7-3.8-4.2l1.1-1.2z" fill="var(--accent)"/>
        </svg>
        (800) 417-2964
      </span>
      <span class="contact-item">
        <svg class="contact-icon" viewBox="0 0 24 24" aria-hidden="true">
          <rect x="1.5" y="5" width="21" height="14" fill="none" stroke="var(--accent)" stroke-width="1.6"/>
          <path d="M1.5 5l10.5 8 10.5-8M1.5 19l7.5-7M22.5 19l-7.5-7" fill="none" stroke="var(--accent)" stroke-width="1.4"/>
        </svg>
        sleep@quorvana.com
      </span>
    </div>
  </section>
</main>
</body>
</html>
```